Shisha Hookah Charcoal Box Packing Design + Logo

Im looking for someone to create a packaging for our cubed shisha charcoal product mainly targeted at the shisha smoking market in the middle east and around the Globe.

I want to see 2 Colour schemes: Black/Gold Black/Copper

Brand Name: "Velvet Ember" and must have the "C" like in the picture attached.

The overall feel of the packaging should be luxury yet fresh and funky with the highest of quality again see the picture attached.

Packaging: Flat / Rectangular

Target Market(s)

Shisha Hookah Smokers in the Middle East and over the globe

Industry/Entity Type

Product

Font styles to use
Script

Requirements
Must have
• The Words "Velvet Ember" and the "C" on the box.

```html
<!DOCTYPE html>
<html lang="en">
<head>
<meta charset="utf-8">
<title>Velvet Ember – Charcoal Box Concepts</title>
<link rel="stylesheet" href="https://fonts.googleapis.com/css2?family=Satisfy&family=Kaushan+Script&family=Lobster&family=Josefin+Sans:wght@400&display=swap">
<style>
  :root {
    --backdrop: #e9e7e3;
    --box-black: #050505;
    --damask-dark: #151515;
    --sun-yellow: #ffc20e;
    --silver-light: #e6e6e6;
    --silver-mid: #a9a9a9;
    --silver-dark: #5e5e5e;
    --floral-grey: #3a3a3a;
    --gold-light: #f7d23a;
    --gold-mid: #c9921a;
    --gold-dark: #6b4a0c;
    --text-white: #ffffff;
    --ink: #111111;
  }
  * { margin: 0; padding: 0; box-sizing: border-box; }
  html, body { width: 732px; height: 1200px; overflow: hidden; }
  body { background: var(--backdrop); position: relative; }

  .box {
    position: absolute;
    width: 672px;
    height: 336px;
    background: var(--box-black);
    overflow: hidden;
    box-shadow: 0 4px 10px rgba(0,0,0,0.35);
  }
  .box--damask { left: 30px; top: 38px;
    background: radial-gradient(ellipse at 50% 40%, var(--damask-dark), var(--box-black) 75%); }
  .box--floral-grey { left: 36px; top: 424px; width: 670px; height: 333px; }
  .box--floral-gold { left: 30px; top: 812px; }

  .brand-title {
    position: absolute; left: 0; right: 0;
    text-align: center; line-height: 1;
    color: var(--sun-yellow);
  }
  .box--damask .brand-title { top: 36px; font-family: "Satisfy", cursive; font-size: 60px; }
  .box--floral-grey .brand-title { top: 42px; font-family: "Kaushan Script", cursive; font-size: 62px; }
  .box--floral-gold .brand-title {
    top: 40px; font-family: "Lobster", cursive; font-size: 58px;
    background: linear-gradient(180deg, var(--gold-light), var(--gold-mid) 70%, var(--gold-dark));
    -webkit-background-clip: text; background-clip: text; color: transparent;
  }

  .tagline {
    position: absolute; left: 0; right: 0;
    text-align: center;
    font-family: "Josefin Sans", sans-serif;
    color: var(--text-white);
    line-height: 1;
  }
  .box--damask .tagline { top: 102px; font-size: 21px; }
  .box--floral-grey .tagline { top: 110px; font-size: 20px; }
  .box--floral-gold .tagline { top: 112px; font-size: 22px; }

  .tagline-rule {
    position: absolute; top: 120px; height: 1px; width: 66px;
    background: var(--text-white);
  }
  .tagline-rule--left { left: 142px; }
  .tagline-rule--right { left: 464px; }

  .grunge-band { position: absolute; top: 0; bottom: 0; background: var(--sun-yellow); }
  .grunge-band--left { left: 0; width: 30px; }
  .grunge-band--right { right: 0; width: 22px; }

  .filigree {
    position: absolute; left: 118px; top: 150px; width: 424px; height: 160px;
    background: radial-gradient(ellipse at 50% 55%, var(--silver-mid) 0%, var(--silver-dark) 45%, rgba(0,0,0,0) 72%);
    opacity: 0.7;
  }

  .floral-corner { position: absolute; top: 0; bottom: 0; }
  .floral-corner--left { left: 0; width: 140px; }
  .floral-corner--right { right: 0; width: 162px; }
  .box--floral-grey .floral-corner--left {
    background: linear-gradient(90deg, var(--floral-grey), rgba(58,58,58,0.35) 70%, rgba(0,0,0,0)); }
  .box--floral-grey .floral-corner--right {
    background: linear-gradient(270deg, var(--floral-grey), rgba(58,58,58,0.35) 70%, rgba(0,0,0,0)); }
  .box--floral-gold .floral-corner--left { width: 150px;
    background: linear-gradient(90deg, var(--gold-dark), rgba(201,146,26,0.45) 60%, rgba(0,0,0,0)); }
  .box--floral-gold .floral-corner--right { width: 166px;
    background: linear-gradient(270deg, var(--gold-dark), rgba(201,146,26,0.45) 60%, rgba(0,0,0,0)); }

  .seal {
    position: absolute; border-radius: 50%;
    display: flex; align-items: center; justify-content: center;
    font-family: "Josefin Sans", sans-serif; font-size: 17px;
    color: var(--ink); text-align: center; line-height: 1.1;
  }
  .box--damask .seal {
    left: 264px; top: 156px; width: 144px; height: 144px;
    background: linear-gradient(90deg, var(--silver-dark), var(--silver-light) 45%, var(--silver-mid));
    border: 3px solid #2a2a2a;
  }
  .box--floral-grey .seal {
    left: 260px; top: 152px; width: 148px; height: 148px;
    background: var(--sun-yellow);
    border: 4px solid var(--silver-mid);
  }
  .box--floral-gold .seal {
    left: 260px; top: 152px; width: 152px; height: 152px;
    background: var(--text-white);
    border: 6px solid var(--gold-mid);
  }
</style>
</head>
<body>

  <section class="box box--damask">
    <div class="grunge-band grunge-band--left" role="img" aria-label="Distressed yellow edge texture"></div>
    <div class="grunge-band grunge-band--right" role="img" aria-label="Distressed yellow edge texture"></div>
    <h1 class="brand-title">Velvet Ember</h1>
    <p class="tagline">Premium Shisha Charcoal</p>
    <div class="filigree" role="img" aria-label="Silver scroll filigree ornament framing the seal"></div>
    <div class="seal">Velvet<br>Ember</div>
  </section>

  <section class="box box--floral-grey">
    <div class="floral-corner floral-corner--left" role="img" aria-label="Grey floral swirl pattern"></div>
    <div class="floral-corner floral-corner--right" role="img" aria-label="Grey floral swirl pattern"></div>
    <h1 class="brand-title">Velvet Ember</h1>
    <span class="tagline-rule tagline-rule--left"></span>
    <p class="tagline">Premium Shisha Charcoal</p>
    <span class="tagline-rule tagline-rule--right"></span>
    <div class="seal">Velvet<br>Ember</div>
  </section>

  <section class="box box--floral-gold">
    <div class="floral-corner floral-corner--left" role="img" aria-label="Gold floral swirl pattern"></div>
    <div class="floral-corner floral-corner--right" role="img" aria-label="Gold floral swirl pattern"></div>
    <h1 class="brand-title">Velvet Ember</h1>
    <p class="tagline">Premium Shisha Charcoal</p>
    <div class="seal">Velvet<br>Ember</div>
  </section>

</body>
</html>
```